Breakfast Cafe - The Sunny Perch

It is for my breakfast and lunch cafe with a hawaiian / beach theme. I am open 7 days a week from 7am to 2pm. We serve traditional American food such as omelettes, pancakes, burgers and sandwiches. I'll upload my old card and my new logo to be used. We have a lot of day to day regulars who eat there during the week, our t-shirts actually say 'Locals Only' on them. Hope this helps. Thanks.

Target Market(s)

anyone who has an appetite!

Industry/Entity Type

American Restaurant

Contact Information for Business Card

7340D Marlin Harbor Road
Long Beach, California
(555) 317-2286

Requirements
Must have
• Address and phone number easily readable.
Nice to have
• beach or tropical theme

```html
<!DOCTYPE html>
<html lang="en">
<head>
<meta charset="utf-8">
<title>The Sunny Perch – Business Card</title>
<link href="https://fonts.googleapis.com/css2?family=Questrial&family=Montserrat:wght@600&family=Oswald:wght@600&display=swap" rel="stylesheet">
<style>
  :root {
    --page: #f4f4f4;
    --sky-top: #27447f;
    --sky-mid: #4a6fa3;
    --sea: #2e8f86;
    --sea-light: #3aa394;
    --sand: #a99a72;
    --wood: #b9732f;
    --logo-disc: #e7a24c;
    --logo-name: #62c3e6;
    --white: #ffffff;
  }
  html, body {
    margin: 0;
    width: 1200px;
    height: 1200px;
    overflow: hidden;
    background: var(--page);
  }
  .stage { position: relative; width: 1200px; height: 1200px; }
  .card {
    position: absolute;
    left: 261px;
    width: 677px;
    height: 387px;
    overflow: hidden;
  }
  .card--front { top: 131px; }
  .card--back { top: 648px; }
  .beach-photo {
    position: absolute;
    inset: 0;
    background:
      linear-gradient(100deg, transparent 55%, rgba(40,90,40,0.35) 80%, rgba(169,154,114,0.5) 100%),
      linear-gradient(180deg, var(--sky-top) 0%, var(--sky-mid) 45%, var(--sea-light) 62%, var(--sea) 100%);
  }
  .logo-disc {
    position: absolute;
    border-radius: 50%;
    background: var(--logo-disc);
    border: 10px solid var(--wood);
    box-sizing: border-box;
  }
  .brand-name {
    position: absolute;
    left: 0; right: 0;
    text-align: center;
    font-family: "Questrial", sans-serif;
    color: var(--logo-name);
    white-space: nowrap;
    line-height: 1;
  }
  .brand-place {
    position: absolute;
    left: 0; right: 0;
    text-align: center;
    font-family: "Oswald", sans-serif;
    font-weight: 600;
    color: var(--wood);
    white-space: nowrap;
    line-height: 1;
  }
  /* front */
  .card--front .logo-disc { left: 238px; top: 36px; width: 200px; height: 200px; }
  .card--front .brand-name { top: 250px; font-size: 42px; }
  .card--front .brand-place { top: 306px; font-size: 14px; letter-spacing: 5px; }
  /* back */
  .band { position: absolute; left: 0; right: 0; background: var(--wood); }
  .band--thin { top: 277px; height: 22px; }
  .band--base { top: 316px; height: 71px; }
  .card--back .logo-disc { left: 125px; top: 56px; width: 140px; height: 140px; }
  .brand-lockup { position: absolute; left: 95px; width: 200px; top: 0; height: 260px; }
  .card--back .brand-name { top: 206px; font-size: 24px; }
  .card--back .brand-place { top: 238px; font-size: 9px; letter-spacing: 3px; }
  .contact {
    position: absolute;
    left: 316px;
    top: 84px;
    color: var(--white);
    font-family: "Questrial", sans-serif;
    font-size: 16px;
    line-height: 20px;
  }
  .contact-row { display: flex; gap: 10px; align-items: flex-start; margin-bottom: 10px; }
  .contact-row svg { flex: none; width: 21px; height: 21px; }
  .hours {
    margin-top: 14px;
    font-family: "Montserrat", sans-serif;
    font-weight: 600;
    font-size: 20px;
    line-height: 27px;
  }
  .hours .time { font-family: "Questrial", sans-serif; font-weight: 400; font-size: 21px; }
</style>
</head>
<body>
<div class="stage">

  <section class="card card--front">
    <div class="beach-photo" role="img" aria-label="Tropical beach photo with palm trees, turquoise water and blue sky"></div>
    <div class="logo-disc"></div>
    <div class="brand-name">The Sunny Perch</div>
    <div class="brand-place">LONG BEACH, CA</div>
  </section>

  <section class="card card--back">
    <div class="beach-photo" role="img" aria-label="Tropical beach photo with palm trees, turquoise water and blue sky"></div>
    <div class="band band--thin"></div>
    <div class="band band--base"></div>
    <div class="logo-disc"></div>
    <div class="brand-lockup">
      <div class="brand-name">The Sunny Perch</div>
      <div class="brand-place">LONG BEACH, CA</div>
    </div>
    <div class="contact">
      <div class="contact-row">
        <svg viewBox="0 0 24 24" aria-hidden="true">
          <circle cx="12" cy="12" r="12" fill="#fff"/>
          <path d="M12 5a5 5 0 0 0-5 5c0 3.6 5 9 5 9s5-5.4 5-9a5 5 0 0 0-5-5z" fill="none" stroke="#3b5a8a" stroke-width="1.8"/>
          <circle cx="12" cy="10" r="1.8" fill="#3b5a8a"/>
        </svg>
        <div>7340D Marlin Harbor Road<br>Long Beach, California</div>
      </div>
      <div class="contact-row">
        <svg viewBox="0 0 24 24" aria-hidden="true">
          <circle cx="12" cy="12" r="12" fill="#fff"/>
          <path d="M8.2 6.5l2 2.3-1.2 1.6c.8 1.7 2 2.9 3.6 3.7l1.6-1.2 2.3 2-1.3 2c-4.6-.5-8.5-4.4-9-9z" fill="#3b5a8a"/>
        </svg>
        <div>(555) 317-2286</div>
      </div>
      <div class="hours">BREAKFAST AND LUNCH<br><span class="time">7am-2pm daily</span></div>
    </div>
  </section>

</div>
</body>
</html>
```